Business Card Design Project

Hi!
Looking for a business card design for my acupuncture/remedial massage business using a logo I've just had designed through this site!
I'd like the following details included:
Logo (obviously)
My name - Marnie Trevaskis
Clinic details -Integrative Wellbeing and Natural Therapies Centre
42 Wendover Street
Ashwood Vale 3189
03 9471 2856
Website - www.trevaskisflow.com.au
I have the logo design in two different colour combinations, one predominantly green, and the other in reverse colours. I was thinking that the green logo would take up one whole side of the business card, then we could include the reverse logo on the more detailed side. I'd like to see how that looks.
I also had the idea that the heart in the logo could be printed in metallic red (depending on cost). Not sure if that comes into play now or at the printers.
Thanks!

```html
<!DOCTYPE html>
<html lang="en">
<head>
<meta charset="utf-8">
<title>Trevaskis Flow – Business Card</title>
<link href="https://fonts.googleapis.com/css2?family=Montserrat:wght@400;600;700&display=swap" rel="stylesheet">
<style>
  :root {
    --brand-green: #1bb68a;
    --card-white: #ffffff;
    --canvas-bg: #ffffff;
    --text-grey: #4a4a4a;
    --text-dark: #333333;
    --card-edge: #d6d6d6;
  }
  * { box-sizing: border-box; margin: 0; padding: 0; }
  html, body {
    width: 1200px;
    height: 1000px;
    overflow: hidden;
    background: var(--canvas-bg);
    font-family: "Montserrat", Arial, sans-serif;
  }
  .card {
    position: absolute;
    top: 72px;
    width: 482px;
    height: 290px;
    border: 1px solid var(--card-edge);
    box-shadow: 0 2px 5px rgba(0,0,0,0.18);
  }
  .card--front { left: 82px; background: var(--card-white); }
  .card--back {
    left: 642px;
    background: var(--brand-green);
    border-color: var(--brand-green);
    display: flex;
    align-items: center;
    justify-content: center;
  }
  .brand-name {
    font-weight: 700;
    line-height: 1;
    display: flex;
    align-items: center;
  }
  .brand-name__dot { border-radius: 50%; flex: none; }
  .card--front .brand-name {
    position: absolute;
    top: 26px;
    left: 26px;
    color: var(--brand-green);
    font-size: 28px;
    gap: 8px;
  }
  .card--front .brand-name__dot {
    width: 12px; height: 12px;
    background: var(--brand-green);
  }
  .card--back .brand-name {
    color: var(--card-white);
    font-size: 56px;
    gap: 16px;
  }
  .card--back .brand-name__dot {
    width: 26px; height: 26px;
    background: var(--card-white);
  }
  .contact {
    position: absolute;
    right: 32px;
    top: 134px;
    text-align: right;
    white-space: nowrap;
  }
  .contact__name {
    color: var(--brand-green);
    font-weight: 700;
    font-size: 16px;
    line-height: 20px;
  }
  .contact__clinic {
    color: var(--text-grey);
    font-size: 11px;
    line-height: 14px;
    margin-top: 4px;
  }
  .contact__address {
    color: var(--text-grey);
    font-size: 13.5px;
    line-height: 18px;
    margin-top: 14px;
  }
  .contact__phone {
    color: var(--text-dark);
    font-weight: 700;
    font-size: 13.5px;
    line-height: 18px;
    margin-top: 9px;
    letter-spacing: 0.4px;
  }
  .contact__web {
    color: var(--brand-green);
    font-size: 14.5px;
    line-height: 18px;
    margin-top: 8px;
  }
</style>
</head>
<body>
  <main class="card-set">
    <section class="card card--front" aria-label="Business card, details side">
      <div class="brand-name">
        <span class="brand-name__dot"></span>
        <span>Trevaskis<br>Flow</span>
      </div>
      <div class="contact">
        <p class="contact__name">Marnie Trevaskis</p>
        <p class="contact__clinic">Integrative Wellbeing and Natural Therapies Centre</p>
        <p class="contact__address">42 Wendover Street, Ashwood Vale 3189</p>
        <p class="contact__phone">03 9471 2856</p>
        <p class="contact__web">www.trevaskisflow.com.au</p>
      </div>
    </section>
    <section class="card card--back" aria-label="Business card, brand side">
      <div class="brand-name">
        <span class="brand-name__dot"></span>
        <span>Trevaskis<br>Flow</span>
      </div>
    </section>
  </main>
</body>
</html>
```